Startup but Passionate F&B Company with big dreams for the future and multiple brands needs business

We need a simple logo and typography design for business card usage for a new company in a bustling and modern city called Marlowe Quay Pte Ltd. We are an F&B company that owns multiple brands of small boutique and indie cafes and eateries. We offer artisanal and home made food created with passion using quality and fresh ingredient. We would like to remain relevant and grow in the future constantly adapting changes and testing new boundaries with our menu and offerings in line with moving tastes and times. Final design and colors should be simple, fresh but modern and will remain relevant in time to come. For fonts we prefer modern fonts such as avenir (meaning future/futuristic) or any other new and trendy font types.
Updates

Please include a logo design as well as typography on th name card.

Thanks

Industry/Entity Type

Boutique

Font styles to use
Other font styles liked:
• Avenir or any other modern looking fonts

Colors

Designer to choose colors to be used in the design.

Requirements
Must have
• Logo + typography

```html
<!DOCTYPE html>
<html lang="en">
<head>
<meta charset="utf-8">
<title>Marlowe Quay Pte Ltd – Business Card</title>
<link rel="stylesheet" href="https://fonts.googleapis.com/css2?family=Exo+2:wght@500;600&family=Ubuntu:wght@400&display=swap">
<style>
  :root {
    --stage: #1b1b1b;
    --card-dark: #141414;
    --card-light: #efefed;
    --brand-green: #6cc04a;
    --ink: #222222;
    --white: #ffffff;
  }
  html, body {
    margin: 0;
    padding: 0;
    width: 1050px;
    height: 1200px;
    overflow: hidden;
    background: var(--stage);
  }
  .canvas {
    position: relative;
    width: 1050px;
    height: 1200px;
  }
  .business-card {
    position: absolute;
    left: 75px;
    top: 342px;
    width: 900px;
    height: 516px;
    background: var(--card-dark);
    box-shadow: 0 20px 50px rgba(0,0,0,0.5);
    overflow: hidden;
  }
  .card-panel {
    position: absolute;
    inset: 0;
  }
  .brand-side {
    position: absolute;
    left: 0;
    top: 0;
    width: 441px;
    height: 516px;
    text-align: center;
    color: var(--white);
  }
  .brand-mark {
    width: 64px;
    height: 64px;
    margin: 168px auto 0;
    background: var(--brand-green);
  }
  .brand-name {
    margin: 24px 0 0;
    font-family: "Exo 2", sans-serif;
    font-weight: 600;
    font-size: 34px;
    line-height: 38px;
    color: var(--white);
  }
  .brand-web {
    position: absolute;
    left: 0;
    right: 0;
    bottom: 26px;
    font-family: "Ubuntu", sans-serif;
    font-size: 19px;
    color: var(--white);
  }
  .contact-side {
    position: absolute;
    left: 477px;
    top: 0;
    right: 30px;
    height: 516px;
  }
  .person-name {
    position: absolute;
    top: 52px;
    margin: 0;
    font-family: "Exo 2", sans-serif;
    font-weight: 500;
    font-size: 44px;
    line-height: 48px;
    color: var(--ink);
  }
  .person-role {
    position: absolute;
    top: 100px;
    margin: 0;
    font-family: "Exo 2", sans-serif;
    font-weight: 500;
    font-size: 30px;
    line-height: 34px;
    color: var(--brand-green);
  }
  .contact-list {
    position: absolute;
    top: 226px;
    margin: 0;
    padding: 0;
    list-style: none;
    font-family: "Ubuntu", sans-serif;
    font-size: 20px;
    line-height: 31px;
    color: var(--ink);
  }
  .contact-label {
    color: var(--brand-green);
  }
</style>
</head>
<body>
<main class="canvas">
  <section class="business-card" aria-label="Business card, Marlowe Quay Pte Ltd">
    <svg class="card-panel" width="900" height="516" viewBox="0 0 900 516" aria-hidden="true">
      <polygon points="441,0 900,0 900,516 441,516 441,144 380,106 441,55" fill="var(--card-light)"/>
    </svg>

    <div class="brand-side">
      <div class="brand-mark"></div>
      <p class="brand-name">Marlowe Quay<br>Pte Ltd.</p>
      <div class="brand-web">www.marlowequay.com</div>
    </div>

    <div class="contact-side">
      <h1 class="person-name">Elena Marsh</h1>
      <p class="person-role">CEO</p>
      <ul class="contact-list">
        <li><span class="contact-label">mobile:</span> +65 6210 4837</li>
        <li><span class="contact-label">phone/fax:</span> +65 6210 4837</li>
        <li><span class="contact-label">add:</span> address line put here</li>
        <li><span class="contact-label">email:</span> hello@marlowequay.com</li>
      </ul>
    </div>
  </section>
</main>
</body>
</html>
```